Cobalt Ridge Goods Co.
Cobalt Ridge Goods Co. business cards - Miscellaneous
Cobalt Ridge Goods Co. business cards
Professional
Trevor Kasmund
President
Denver | Colorado | USA
trev@cobaltridgegoods.example
www.cobaltridgegoods.example
I would like the logo to be on the front of the business card preferably the size of the height of the card on the left side
I would like the logo to be on the back of the business card as well. The logo should take up the entire back of the business card.
quartzfen quartzfen
Kindly do some star rating... it will really help us to make stationary for your like designs.. thanks!
kasmundtk kasmundtk
We are also looking for at stationary options. Please provide any options for letterhead, etc..

```html
<!DOCTYPE html>
<html lang="en">
<head>
<meta charset="utf-8">
<title>Cobalt Ridge Goods Co. — Business Cards</title>
<link href="https://fonts.googleapis.com/css2?family=PT+Sans:wght@400;700&display=swap" rel="stylesheet">
<style>
  :root {
    --backdrop: #8c8c8c;
    --navy: #24216f;
    --paper: #ffffff;
    --ink-grey: #7a7a7a;
    --accent-red: #d8222a;
  }
  * { box-sizing: border-box; margin: 0; padding: 0; }
  html, body {
    width: 1200px; height: 871px; overflow: hidden;
    background: var(--backdrop);
    font-family: "PT Sans", Arial, sans-serif;
  }
  .sheet { position: relative; width: 1200px; height: 871px; }

  .card { position: absolute; }

  /* Front */
  .card-front {
    left: 60px; top: 252px; width: 640px; height: 366px;
    background: var(--paper);
  }
  .front-logo {
    position: absolute; left: 34px; top: 34px; width: 250px; height: 298px;
    display: flex; flex-direction: column; justify-content: center;
    color: var(--navy); font-weight: 700; line-height: 0.95;
  }
  .front-logo .word { font-size: 58px; letter-spacing: -0.5px; }
  .front-logo .word-last { display: flex; align-items: center; gap: 12px; }
  .logo-square { width: 26px; height: 26px; background: var(--navy); }

  .identity {
    position: absolute; right: 30px; top: 30px; text-align: right;
  }
  .identity .person { color: var(--navy); font-weight: 700; font-size: 22px; }
  .identity .role { color: var(--ink-grey); font-size: 15px; margin-top: 2px; }

  .contact {
    position: absolute; left: 322px; top: 178px;
    color: var(--ink-grey); font-size: 16px; line-height: 1.55;
  }
  .contact .place { color: #5e5e5e; font-weight: 700; margin-bottom: 12px; font-size: 15px; }
  .contact .web { color: var(--accent-red); font-weight: 700; margin-top: 10px; }

  /* Back */
  .card-back {
    left: 774px; top: 115px; width: 366px; height: 640px;
    background: var(--navy); color: var(--paper);
  }
  .back-logo {
    position: absolute; left: 36px; top: 40px; width: 294px; height: 470px;
    display: flex; flex-direction: column; justify-content: center;
    font-weight: 700; line-height: 0.95;
  }
  .back-logo .word { font-size: 78px; letter-spacing: -1px; }
  .back-logo .word-last { display: flex; align-items: center; gap: 14px; }
  .back-logo .logo-square { width: 34px; height: 34px; background: var(--paper); }
  .back-web {
    position: absolute; left: 0; right: 0; bottom: 80px;
    text-align: center; font-size: 16px; font-weight: 700;
  }
</style>
</head>
<body>
  <main class="sheet">
    <section class="card card-front" aria-label="Business card front">
      <div class="front-logo" aria-label="Cobalt Ridge Goods Co.">
        <span class="word">COBALT</span>
        <span class="word">RIDGE</span>
        <span class="word">GOODS</span>
        <span class="word word-last">CO.<span class="logo-square"></span></span>
      </div>

      <div class="identity">
        <p class="person">Trevor Kasmund</p>
        <p class="role">President</p>
      </div>

      <div class="contact">
        <p class="place">Denver | Colorado | USA</p>
        <p class="phone">720.555.0148</p>
        <p class="email">trev@cobaltridgegoods.example</p>
        <p class="web">www.cobaltridgegoods.example</p>
      </div>
    </section>

    <section class="card card-back" aria-label="Business card back">
      <div class="back-logo" aria-label="Cobalt Ridge Goods Co.">
        <span class="word">COBALT</span>
        <span class="word">RIDGE</span>
        <span class="word">GOODS</span>
        <span class="word word-last">CO.<span class="logo-square"></span></span>
      </div>
      <p class="back-web">www.cobaltridgegoods.example</p>
    </section>
  </main>
</body>
</html>
```